Coffee Shop needs a fresh new menu

Hi,
I would like a new menu to be designed for our coffee shop.
We display our menu on a television screen, so would need it in a file that would allow us to continue to do so -- I have attached a photo so that you can see our current design, and how it is displayed.

I'd like something that is easy to read, if the design could have a "hipster" feel to it -- we are located at a hospital and University.

I have attached a Word file with what we would like on the menu.

Feel free to contact me if you have any questions.

Thanks,
Liv

Just A4 size will be fine, and no need to include menu 1 and menu 2 - I just put them in as an example of what we already have -- they are our printed menu's. Thanks

Hospital

```html
<!DOCTYPE html>
<html lang="en">
<head>
<meta charset="utf-8">
<title>Menu</title>
<link rel="stylesheet" href="https://fonts.googleapis.com/css2?family=Lato:wght@700;900&family=Stardos+Stencil:wght@700&display=swap">
<style>
:root{
  --board-light:#3b3b3b;
  --board-mid:#262626;
  --board-dark:#121212;
  --chalk:#f2f2f2;
  --text:#ffffff;
  --band:rgba(255,255,255,0.24);
  --band-soft:rgba(255,255,255,0.03);
}
*{margin:0;padding:0;box-sizing:border-box}
html,body{width:1200px;height:848px;overflow:hidden}
body{
  position:relative;
  background:radial-gradient(ellipse at 50% 45%,var(--board-light) 0%,var(--board-mid) 45%,var(--board-dark) 100%);
  font-family:"Lato",Arial,sans-serif;
  color:var(--text);
}
.chalk-frame{position:absolute;inset:0;width:1200px;height:848px}
.menu-title{
  position:absolute;top:28px;left:0;width:1200px;text-align:center;
  font-family:"Stardos Stencil",Impact,sans-serif;font-weight:700;
  font-size:46px;letter-spacing:1px;line-height:1;color:var(--chalk);
}
.section-heading{
  position:absolute;font-weight:900;font-size:30px;line-height:1;letter-spacing:-0.3px;
}
.item-list{position:absolute;list-style:none}
.item{
  display:flex;align-items:center;height:34px;
  font-weight:700;font-size:20px;
}
.item:nth-child(odd){
  background:linear-gradient(90deg,transparent 0%,var(--band) 7%,var(--band) 93%,transparent 100%);
}
.item:nth-child(even){
  background:linear-gradient(90deg,transparent 0%,var(--band-soft) 10%,var(--band-soft) 90%,transparent 100%);
}
.item-name{flex:1}
.item-price{width:90px}
.left-col{left:97px;width:463px}
.left-col .item{padding-left:31px}
.left-col .item-price{margin-right:0}
.right-col{left:632px;width:468px}
.right-col .item{padding-left:31px}
.right-col .item-price{width:92px}
.heading-light{left:128px;top:96px}
.heading-breakfast{left:128px;top:428px}
.heading-hot{left:663px;top:96px}
.list-light{top:138px}
.list-breakfast{top:469px}
.list-hot{top:138px}
.store-note{
  position:absolute;left:632px;top:607px;width:468px;height:98px;
  padding:12px 0 0 31px;
  background:linear-gradient(90deg,transparent 0%,rgba(255,255,255,0.2) 7%,rgba(255,255,255,0.2) 93%,transparent 100%);
  font-weight:700;font-size:17px;line-height:24.5px;
}
</style>
</head>
<body>
<svg class="chalk-frame" viewBox="0 0 1200 848" aria-hidden="true">
  <g fill="none" stroke="var(--chalk)" stroke-width="2.5" stroke-linecap="round" opacity="0.9">
    <path d="M495 48 H50 V802 H1147 V48 H705"/>
    <path d="M495 64 H35 V790 H1162 V64 H705"/>
    <path d="M52 52 H493 M707 52 H1143" stroke-width="1" opacity="0.6"/>
  </g>
</svg>

<h1 class="menu-title">MENU</h1>

<h2 class="section-heading heading-light">Something Light:</h2>
<ul class="item-list left-col list-light">
  <li class="item"><span class="item-name">Mixed Yoghurts</span><span class="item-price">$5.50</span></li>
  <li class="item"><span class="item-name">Chia Pudding</span><span class="item-price">$5.50</span></li>
  <li class="item"><span class="item-name">Fruit Salad</span><span class="item-price">$5.50</span></li>
  <li class="item"><span class="item-name">Bircher Muesli</span><span class="item-price">$5.50</span></li>
  <li class="item"><span class="item-name">Protein Balls</span><span class="item-price">$4.00</span></li>
  <li class="item"><span class="item-name">Banana Bread</span><span class="item-price">$4.50</span></li>
  <li class="item"><span class="item-name">Muffins</span><span class="item-price">$4.50</span></li>
  <li class="item"><span class="item-name">Slices</span><span class="item-price">$4.00</span></li>
</ul>

<h2 class="section-heading heading-breakfast">Breakfast Items:</h2>
<ul class="item-list left-col list-breakfast">
  <li class="item"><span class="item-name">Bacon, Egg and Cheese Roll</span><span class="item-price">$6.00</span></li>
  <li class="item"><span class="item-name">Ham and Cheese Toastie</span><span class="item-price">$5.00</span></li>
  <li class="item"><span class="item-name">Cheese and Tomato Toastie</span><span class="item-price">$5.00</span></li>
  <li class="item"><span class="item-name">Ham and Cheese Croissant</span><span class="item-price">$6.00</span></li>
  <li class="item"><span class="item-name">Cheese and Tomato Croissant</span><span class="item-price">$5.50</span></li>
  <li class="item"><span class="item-name">Plain Croissant</span><span class="item-price">$3.50</span></li>
  <li class="item"><span class="item-name">Hash Brown</span><span class="item-price">$2.00</span></li>
  <li class="item"><span class="item-name">2 Piece Toast</span><span class="item-price">$3.00</span></li>
  <li class="item"><span class="item-name">2 Piece Rasin Toast</span><span class="item-price">$3.00</span></li>
</ul>

<h2 class="section-heading heading-hot">Hot Food and Sandwiches:</h2>
<ul class="item-list right-col list-hot">
  <li class="item"><span class="item-name">Pre Made Sandwiches</span><span class="item-price">$6.50</span></li>
  <li class="item"><span class="item-name">Pre Made Sandwiches</span><span class="item-price">$7.50</span></li>
  <li class="item"><span class="item-name">Pre Made Focaccias</span><span class="item-price">$8.50</span></li>
  <li class="item"><span class="item-name">Wraps</span><span class="item-price">$7.50</span></li>
  <li class="item"><span class="item-name">Vegetarian Salad</span><span class="item-price">$7.50</span></li>
  <li class="item"><span class="item-name">Meat/Seafood Salad</span><span class="item-price">$9.50</span></li>
  <li class="item"><span class="item-name">Hot Chips</span><span class="item-price">$4.50</span></li>
  <li class="item"><span class="item-name">Dim Sim</span><span class="item-price">$1.50</span></li>
  <li class="item"><span class="item-name">Potato Cake</span><span class="item-price">$1.50</span></li>
  <li class="item"><span class="item-name">Plain Hamburger</span><span class="item-price">$7.50</span></li>
  <li class="item"><span class="item-name">Hamburger with the lot</span><span class="item-price">$9.00</span></li>
  <li class="item"><span class="item-name">Chicken Schnitzel Burger</span><span class="item-price">$8.50</span></li>
</ul>

<p class="store-note">Our Store inside the Hospital Food Court sells:<br>Hot Pies, Assorted Pasta's, Ready-to-go Meals,<br>Quiche, and lots more!</p>
</body>
</html>
```